Quarrow financial services, is a financial company that provides consultancy, brokerage services, and funding.

we will be providing the clients with insights, knowledge and data with regards to the financial markets.

with the brokerage services we will try to find the suitable counterparts that provide them with the best investments that suits their needs and expected return.

Target Market(s)

financial institutions, Corporates, high-net worth individuals

Industry/Entity Type

Financial Service

Contact Information for Business Card

Font styles to use
Other font styles liked:
• applemyungjo

Colors
00a990
848484

Requirements
Must have
• the logo at the back
Nice to have
• Finesse
Should not have
• boldness

```html
<!DOCTYPE html>
<html lang="en">
<head>
<meta charset="utf-8">
<title>Quarrow Financial Services – Business Card</title>
<link href="https://fonts.googleapis.com/css2?family=Cinzel:wght@400&family=Questrial&display=swap" rel="stylesheet">
<style>
  :root {
    --backdrop: #3b3b3b;
    --card: #ffffff;
    --ink: #3f4648;
    --muted: #848484;
    --rule: #d0d0d0;
  }
  html, body {
    margin: 0;
    padding: 0;
    width: 1200px;
    height: 900px;
    overflow: hidden;
    background: var(--backdrop);
  }
  .canvas {
    position: relative;
    width: 1200px;
    height: 900px;
  }
  .card {
    position: absolute;
    top: 301px;
    width: 514px;
    height: 297px;
    background: var(--card);
  }
  .card--back { left: 72px; }
  .card--front { left: 615px; }

  .brand {
    position: absolute;
    left: 40px;
    top: 172px;
    width: 195px;
    text-align: center;
  }
  .brand__name {
    display: inline-flex;
    align-items: center;
    gap: 10px;
    font-family: "Cinzel", serif;
    font-weight: 400;
    font-size: 30px;
    line-height: 32px;
    letter-spacing: 1px;
    color: var(--ink);
    white-space: nowrap;
  }
  .brand__dot {
    width: 9px;
    height: 9px;
    border-radius: 50%;
    background: var(--muted);
  }
  .brand__line {
    display: block;
    margin-top: 8px;
    font-family: "Questrial", sans-serif;
    font-size: 9.5px;
    letter-spacing: 0.6px;
    color: var(--muted);
    white-space: nowrap;
  }

  .divider {
    position: absolute;
    left: 258px;
    top: 65px;
    width: 1px;
    height: 166px;
    background: var(--rule);
  }
  .person {
    position: absolute;
    left: 288px;
    top: 71px;
    color: var(--ink);
    font-family: "Cinzel", serif;
  }
  .person__name {
    margin: 0;
    font-size: 17px;
    font-weight: 400;
    line-height: 20px;
    letter-spacing: 0.3px;
  }
  .person__role {
    margin: 0;
    font-size: 9px;
    line-height: 12px;
    letter-spacing: 0.6px;
  }
  .contact {
    position: absolute;
    left: 288px;
    top: 133px;
    margin: 0;
    padding: 0;
    list-style: none;
    font-family: "Questrial", sans-serif;
    font-size: 11.5px;
    line-height: 14px;
    color: var(--ink);
  }
  .contact__label {
    display: inline-block;
    width: 15px;
    color: var(--muted);
  }
  .address {
    position: absolute;
    left: 288px;
    top: 190px;
    margin: 0;
    font-style: normal;
    font-family: "Questrial", sans-serif;
    font-size: 11.5px;
    line-height: 14.5px;
    color: var(--ink);
  }
</style>
</head>
<body>
<main class="canvas">
  <section class="card card--back" aria-label="Card back">
    <div class="brand">
      <span class="brand__name"><span class="brand__dot"></span>QUARROW</span>
      <span class="brand__line">Financial services · insight · funding</span>
    </div>
  </section>

  <section class="card card--front" aria-label="Card front">
    <div class="brand">
      <span class="brand__name"><span class="brand__dot"></span>QUARROW</span>
      <span class="brand__line">Financial services · insight · funding</span>
    </div>
    <div class="divider"></div>
    <div class="person">
      <h1 class="person__name">Daniel Marrick</h1>
      <p class="person__role">managing director</p>
    </div>
    <ul class="contact">
      <li><span class="contact__label">p</span>555 014 27 63</li>
      <li><span class="contact__label">m</span>555 019 48 20</li>
      <li><span class="contact__label">e</span>d.marrick@quarrowfinancial.com</li>
    </ul>
    <address class="address">
      48 Sample Lane<br>
      Lakeview, New York 10101<br>
      www.quarrowfinancial.com
    </address>
  </section>
</main>
</body>
</html>
```